Brindle Ecommerce Website Design - Korvel & Pelstry Growth *

The goal of this website is to show case studies and testimonials for Brindle Ecommerce. Our company specializes in Korvel and Pelstry management and growth. The design should communicate trust, growth, and attention to detail.

Below are 3 leading websites in the space
https://quillbrookpartners.com/solutions
https://dorvanstudio.com/
https://velmora.com/

Target Market(s)

Businesses looking to grow on Korvel. Small and large businesses are our clients. Many are brands that are household names.

Industry/Entity Type

Ecommerce

Number of Pages Required

5+ page

Font styles to use
Serif
Sans Serif

```html
<!DOCTYPE html>
<html lang="en">
<head>
<meta charset="utf-8">
<title>Brindle Ecommerce – Insights</title>
<link href="https://fonts.googleapis.com/css2?family=Rubik:wght@300;400;500;700&family=Lato:wght@400;700&display=swap" rel="stylesheet">
<style>
:root{
  --green:#00a63c;
  --green-dark:#0a7a2e;
  --ink:#1d1d1d;
  --text:#2a2a2a;
  --footer:#2a2a2b;
  --panel:#e4e4e4;
  --white:#ffffff;
}
*{margin:0;padding:0;box-sizing:border-box}
html,body{width:723px;height:1200px;overflow:hidden;background:var(--white)}
body{position:relative;font-family:"Rubik",sans-serif;color:var(--text)}

.site-header{position:absolute;left:0;top:0;width:723px;height:42px;background:var(--white)}
.brand{position:absolute;display:flex;align-items:center;gap:5px}
.brand-dot{border-radius:50%;background:var(--green);flex:none}
.brand-name{font-family:"Rubik",sans-serif;font-weight:400;white-space:nowrap}
.site-header .brand{left:67px;top:7px}
.site-header .brand-dot{width:28px;height:28px}
.site-header .brand-name{font-size:13px;color:var(--ink)}
.nav a{position:absolute;top:16px;font-size:8.3px;font-weight:500;color:var(--ink);text-decoration:none;white-space:nowrap}
.nav a.active{color:var(--green)}
.cta{position:absolute;left:531px;top:0;width:125px;height:42px;background:var(--green);color:var(--white);font-size:9px;font-weight:700;display:flex;align-items:center;justify-content:center;letter-spacing:.1px}

.hero{position:absolute;left:0;top:42px;width:723px;height:196px;background:linear-gradient(100deg,#3a4a55 0%,#6d7a80 30%,#9a9690 55%,#6b625c 80%,#3e3a38 100%)}
.hero h1{position:absolute;left:0;right:0;top:80px;text-align:center;color:var(--white);font-size:29px;font-weight:700;letter-spacing:.5px}

.photo{position:absolute;left:67px;top:303px;width:400px;height:247px;background:linear-gradient(120deg,#c9c9cb 0%,#8e8b8a 45%,#4c4e58 75%,#2f3240 100%)}
.details{position:absolute;left:481px;top:303px;width:174px;height:247px;background:linear-gradient(160deg,#00a93e 0%,#05983a 55%,#0a7a2e 100%);color:var(--white)}
.details h2{position:absolute;left:16px;top:21px;font-size:15.5px;font-weight:500;letter-spacing:.2px}
.details dl{font-size:9px;font-weight:500}
.details dt,.details dd{position:absolute;white-space:nowrap}
.details dt{left:16px}
.details dd{left:95px}

.article h2{position:absolute;left:67px;top:576px;font-size:16.5px;font-weight:500;color:var(--ink);letter-spacing:.2px}
.article p{position:absolute;left:67px;font-size:9.8px;font-weight:400;line-height:14.5px;color:var(--text);letter-spacing:.38px}
.article .p1{top:606px;width:396px}
.article .p2{top:661px;width:396px}
.article .p3{top:777px;width:580px;line-height:15.5px}

.brochure{position:absolute;left:481px;top:585px;width:174px;height:161px;background:var(--panel)}
.brochure h3{position:absolute;left:17px;top:27px;font-size:16.5px;font-weight:500;color:var(--ink)}
.brochure p{position:absolute;left:17px;top:53px;width:148px;font-size:7.7px;line-height:13.4px;font-weight:400;color:#333;letter-spacing:.25px}
.download{position:absolute;left:17px;top:116px;width:125px;height:31px;border-radius:16px;background:var(--green);color:var(--white);font-size:9.5px;font-weight:500;padding-left:18px;display:flex;align-items:center;box-shadow:0 2px 4px rgba(0,0,0,.15)}
.download .arrow{position:absolute;right:4px;top:5px;width:22px;height:22px;border-radius:50%;background:var(--white)}

.footer-shape{position:absolute;left:0;top:870px}
.footer{position:absolute;left:0;top:0;width:723px;height:1200px;pointer-events:none;font-family:"Lato",sans-serif}
.footer .brand{left:68px;top:1004px}
.footer .brand-dot{width:34px;height:34px}
.footer .brand-name{font-size:16px;color:var(--white)}
.social span{position:absolute;top:1063px;width:30px;height:30px;border-radius:50%;background:var(--green)}
.footer h4{position:absolute;top:979px;font-size:10.3px;font-weight:700;color:var(--white);letter-spacing:.6px}
.footer h4::after{content:"";position:absolute;left:0;top:17px;width:25px;height:1.5px;background:var(--white)}
.footer ul{list-style:none}
.footer li{position:absolute;font-size:8.3px;font-weight:700;color:#e6e6e6;white-space:nowrap;padding-left:10px}
.footer li::before{content:"";position:absolute;left:0;top:3.5px;width:3px;height:3px;border-radius:50%;background:#e6e6e6}
.contact-line{position:absolute;left:542px;font-size:8.3px;font-weight:700;color:#e6e6e6;line-height:15.5px;white-space:nowrap}
.contact-icon{position:absolute;left:520px}

.bottom-bar{position:absolute;left:0;top:1159px;width:723px;height:41px;background:var(--green);font-family:"Lato",sans-serif;color:var(--white);font-size:9.3px}
.bottom-bar span{position:absolute;top:15px;white-space:nowrap}
.bottom-bar .copy{left:67px;font-weight:700}
.bottom-bar .sep{position:absolute;left:577px;top:9px;width:1px;height:22px;background:rgba(255,255,255,.4)}
.to-top{position:absolute;left:666px;top:1147px;width:22px;height:22px;border-radius:50%;background:var(--white);box-shadow:0 1px 3px rgba(0,0,0,.2)}
</style>
</head>
<body>

<header class="site-header">
  <div class="brand"><span class="brand-dot"></span><span class="brand-name">Brindle Ecommerce</span></div>
  <nav class="nav">
    <a style="left:264px">Home</a>
    <a style="left:312px">Services</a>
    <a style="left:371px">Case Studies</a>
    <a style="left:443px">About</a>
    <a class="active" style="left:488px">Insights</a>
  </nav>
  <div class="cta">FREE CONSULTATION</div>
</header>

<section class="hero" role="img" aria-label="Team working together at laptops in an office">
  <h1>INSIGHTS</h1>
</section>

<div class="photo" role="img" aria-label="Two colleagues reviewing work on a desktop monitor"></div>

<aside class="details">
  <h2>INSIGHTS DETAILS</h2>
  <dl>
    <dt style="top:53px">Category:</dt><dd style="top:53px">IT Technology</dd>
    <dt style="top:82px">Client:</dt><dd style="top:82px">Tovin</dd>
    <dt style="top:110px">Location:</dt><dd style="top:110px">Usa</dd>
    <dt style="top:139px">Completed Date:</dt><dd style="top:139px">2020</dd>
    <dt style="top:168px">Project Value:</dt><dd style="top:168px">50k</dd>
    <dt style="top:197px">Mananer:</dt><dd style="top:197px">Halvorne</dd>
  </dl>
</aside>

<article class="article">
  <h2>BRINDLE ECOMMERCE INSIGHTS</h2>
  <p class="p1">At vero eos et accusamus et iusto odio dignissimos ducimus qui blanditiis praesentium voluptatum deleniti atque corrupti quos dolores et quas molestias excepturi sint occaecati cupiditate non provident, similique sunt in culpa qui.</p>
  <p class="p2">Sed ut perspiciatis unde omnis iste natus error sit voluptatem accusantium doloremque laudantium, totam rem aperiam, eaque ipsa quae ab illo inventore veritatis et quasi architecto beatae vitae dicta sunt explicabo. Nemo enim ipsam voluptatem quia voluptas sit aspernatur aut odit aut fugit, sed quia consequuntur magni dolores eos qui ratione voluptatem sequi nesciunt. Nemo enim ipsam voluptatem quia voluptas sit aspernatur aut odit aut fugit, sed quia consequuntur magni dolores eos qui ratione voluptatem sequi nes.</p>
  <p class="p3">Sed ut perspiciatis unde omnis iste natus error sit voluptatem accusantium doloremque laudantium, totam rem aperiam, eaque ipsa quae ab illo inventore veritatis et quasi architecto beatae vitae dicta sunt explicabo. Nemo enim ipsam voluptatem quia voluptas sit aspernatur aut odit aut fugit, sed quia consequuntur magni dolores eos qui ratione voluptatem sequi nesciunt.</p>
</article>

<aside class="brochure">
  <h3>Brochures</h3>
  <p>At vero eos et accusamus et iusto odio dignissimos ducimus qui blanditiis praesentium voluptatum deleniti atque corrupti.</p>
  <div class="download">DOWNLOAD
    <span class="arrow"><svg width="22" height="22" viewBox="0 0 22 22"><path d="M6.5 11h9M12 7.5l3.5 3.5-3.5 3.5" fill="none" stroke="#00a63c" stroke-width="1.4" stroke-linecap="round" stroke-linejoin="round"/></svg></span>
  </div>
</aside>

<svg class="footer-shape" width="723" height="290" viewBox="0 0 723 290">
  <path d="M0 70 Q361.5 -22 723 70 L723 290 L0 290 Z" fill="#00a63c"/>
  <path d="M0 78 Q361.5 -2 723 78 L723 290 L0 290 Z" fill="#2a2a2b"/>
</svg>

<footer class="footer">
  <div class="brand"><span class="brand-dot"></span><span class="brand-name">Brindle Ecommerce</span></div>
  <div class="social" aria-label="Social links">
    <span style="left:114px"></span><span style="left:150px"></span><span style="left:188px"></span>
  </div>

  <h4 style="left:277px">QUICK LINKS</h4>
  <ul>
    <li style="left:277px;top:1009px">HOME</li>
    <li style="left:277px;top:1026px">SERVICES</li>
    <li style="left:277px;top:1043px">CASE STUDIES</li>
    <li style="left:277px;top:1060px">ABOUT</li>
    <li style="left:277px;top:1077px">INSIGHTS</li>
  </ul>

  <h4 style="left:388px">LINKS</h4>
  <ul>
    <li style="left:388px;top:1009px">FAQ'S</li>
    <li style="left:388px;top:1026px">TERMS &amp; CONDITIONS</li>
    <li style="left:388px;top:1043px">PRIVACY POLICY</li>
  </ul>

  <h4 style="left:522px">CONTACT US</h4>
  <svg class="contact-icon" style="top:1008px" width="11" height="14" viewBox="0 0 11 14"><path d="M5.5 0C2.5 0 0 2.4 0 5.4 0 9.4 5.5 14 5.5 14S11 9.4 11 5.4C11 2.4 8.5 0 5.5 0Z" fill="#fff"/><circle cx="5.5" cy="5.3" r="2" fill="#2a2a2b"/></svg>
  <div class="contact-line" style="top:1006px">418 Larkmoor Avenue, Fenwick<br>Ohio, 44021, USA</div>
  <svg class="contact-icon" style="top:1051px" width="11" height="11" viewBox="0 0 11 11"><path d="M2.2 0.3 3.9 2.4 2.9 3.6C3.6 5.1 5.9 7.4 7.4 8.1L8.6 7.1 10.7 8.8 9.6 10.6C5 10.6 0.4 6 0.4 1.4Z" fill="#fff"/></svg>
  <div class="contact-line" style="top:1051px">555-204-7318</div>
  <svg class="contact-icon" style="top:1079px" width="13" height="9" viewBox="0 0 13 9"><rect x="0.5" y="0.5" width="12" height="8" fill="none" stroke="#fff"/><path d="M0.5 0.5 6.5 5 12.5 0.5M0.5 8.5 5 4.2M12.5 8.5 8 4.2" fill="none" stroke="#fff"/></svg>
  <div class="contact-line" style="top:1077px">hello@brindle-ecom.test</div>
</footer>

<div class="bottom-bar">
  <span class="copy">© 2021 Brindle Ecommerce.&nbsp; All rights reserved</span>
  <span style="left:508px">Privacy policy</span>
  <i class="sep"></i>
  <span style="left:590px">Terms of service</span>
</div>
<div class="to-top"><svg width="22" height="22" viewBox="0 0 22 22"><path d="M8.5 12.3 11 9.8l2.5 2.5" fill="none" stroke="#00a63c" stroke-width="1.3" stroke-linecap="round"/></svg></div>

</body>
</html>
```